Norquel Cardiac Technologies

There is three component of my company
1- device ( heart Monitoring) and related software sales and Marketing
2- we do 24 hrs and 7 days of live streaming monitoring and provide daily and end of study reports to doctors
3- we also provide software and Rhythm interpretation training
Updates

Target Market(s)

hospitals and other small facilities . Technology itself called MCOT ( mobile Cardiac outpatient telemetry .

Industry/Entity Type

Healthcare

Font styles to use
Sans Serif

Requirements
Must have
• Refrences..
• Caldexa technologies.
• - quorvandixa ( taplor)
• - brovaline
• - dune harbor
Nice to have
• Refrences..
• -Caldexa technologies.
• - brovaline
• - dune harbor
Should not have
• Refrences..
• -Caldexa technologies.
• - brovaline
• - dune harbor

```html
<!DOCTYPE html>
<html lang="en">
<head>
<meta charset="utf-8">
<title>Norquel Cardiac Technologies – Brochure</title>
<link href="https://fonts.googleapis.com/css2?family=Arimo:wght@400;700&display=swap" rel="stylesheet">
<style>
:root{
  --navy:#1f4e79;
  --blue:#3b9fe0;
  --blue-mid:#5ab4ef;
  --blue-light:#8fd0f7;
  --band-pale:#cfe8f8;
  --band-soft:#a9d6f3;
  --white:#ffffff;
  --ink:#111111;
  --grid:#9aa3ab;
  --screen-bg:#f5f0c8;
  --screen-line:#d7cfa0;
}
*{box-sizing:border-box;margin:0;padding:0}
html,body{width:1200px;height:900px;overflow:hidden;background:var(--white);font-family:'Arimo',Arial,sans-serif;color:var(--ink)}
.brochure{position:relative;width:1200px;height:900px;display:grid;grid-template-columns:400px 400px 400px;grid-template-rows:450px 450px}
.panel{position:relative;overflow:hidden}

.bg-white{background:var(--white)}
.bg-blue{background:linear-gradient(90deg,var(--blue-light) 0%,var(--blue-mid) 35%,var(--blue) 60%,var(--blue-mid) 100%)}
.bg-bands{background:linear-gradient(180deg,var(--band-soft) 0 18%,var(--white) 18% 30%,var(--band-pale) 30% 62%,var(--band-soft) 62% 80%,var(--band-pale) 80% 100%)}

.label-box{position:absolute;left:30px;width:138px;background:var(--navy);color:var(--white);font-size:15px;font-weight:400;line-height:1.2;padding:12px 9px}
.label-box.top{top:40px}
.label-box.bottom{top:36px}

.sheet{position:absolute;left:178px;top:10px;width:202px;height:390px;background:var(--white);box-shadow:0 2px 6px rgba(0,0,0,.25)}
.compare{position:absolute;left:186px;width:186px;background:var(--white);border-collapse:collapse;font-size:4.6px;line-height:1.15;table-layout:fixed}
.compare.top{top:40px}
.compare.bottom{top:22px}
.compare th,.compare td{border:0.6px solid var(--grid);padding:1px;text-align:center;vertical-align:top;overflow:hidden}
.compare th{font-weight:400}
.compare .row{text-align:left;width:52px}

.heading{position:absolute;left:0;width:100%;text-align:center;font-size:19px;font-weight:400}
.heading.light{color:var(--white)}
.heading.right{font-size:17px}

.screen{position:absolute;background:linear-gradient(180deg,var(--screen-bg),#fbf8e2);border:1px solid var(--screen-line)}
.screen.twa{left:20px;top:90px;width:228px;height:180px}
.screen.qtc{left:14px;top:62px;width:236px;height:205px}
.screen.afib{left:14px;top:80px;width:206px;height:150px}
.screen.report{left:92px;top:20px;width:206px;height:245px;background:linear-gradient(180deg,#fdf7c2,#fffbe2);box-shadow:0 2px 6px rgba(0,0,0,.25)}

.points{position:absolute;list-style:none;font-size:10.5px;line-height:1.2}
.points li{position:relative;padding-left:10px;margin-bottom:10px}
.points li::before{content:"";position:absolute;left:0;top:4px;width:4px;height:4px;border-radius:50%;background:currentColor}
.points.twa{left:274px;top:92px;width:120px;color:var(--white)}
.points.qtc{left:266px;top:62px;width:128px}
.points.afib{left:232px;top:58px;width:134px}

.chevron{position:absolute;top:420px;width:16px;height:44px}
.chevron.left{left:396px}
.chevron.right{left:790px}
</style>
</head>
<body>
<main class="brochure">

  <section class="panel bg-white">
    <h2 class="label-box top">Competitive Comparisons Real-Time Outpatient Cardiac Telemetry</h2>
    <table class="compare top">
      <tr><th class="row"></th><th>Ostrel Telemetry</th><th>Dune Harbor Model A3</th><th>Velmora Unit 10</th><th>Pexano Line S</th><th>Taplor Patch X</th><th>Halvix Band R</th><th>Brovaline Strip M</th></tr>
      <tr><td class="row">Electrode #</td><td>8</td><td>3</td><td>3</td><td>2</td><td>3</td><td>3</td><td>3</td></tr>
      <tr><td class="row">ECG Leads</td><td>8</td><td>2</td><td>2</td><td>1</td><td>2</td><td>2</td><td>2</td></tr>
      <tr><td class="row">Meets CMS coverage policy for real-time ECG monitoring</td><td>YES</td><td>NO</td><td>NO</td><td>YES</td><td>NO</td><td>NO</td><td>NO</td></tr>
      <tr><td class="row">Center archiving of all ECG reports for seven years</td><td>YES</td><td>NO</td><td>NO</td><td>NO</td><td>NO</td><td>?</td><td>NO</td></tr>
      <tr><td class="row">Archiving of full disclosure ECG for seven years</td><td>YES</td><td>NO</td><td>NO</td><td>NO</td><td>NO</td><td>?</td><td>NO</td></tr>
      <tr><td class="row">Sustained V-Tach at HR &gt; 100 bpm</td><td>YES</td><td>NO</td><td>NO</td><td>NO</td><td>NO</td><td>NO</td><td>NO</td></tr>
      <tr><td class="row">Auto Ischemia ST Analysis</td><td>YES</td><td>NO</td><td>NO</td><td>NO</td><td>NO</td><td>NO</td><td>NO</td></tr>
      <tr><td class="row">T-Wave Alternans Analysis</td><td>YES</td><td>NO</td><td>NO</td><td>NO</td><td>NO</td><td>NO</td><td>NO</td></tr>
      <tr><td class="row">Pacemaker Analysis</td><td>YES</td><td>NO</td><td>NO</td><td>NO</td><td>NO</td><td>NO</td><td>NO</td></tr>
      <tr><td class="row">Elongated QTc Analysis</td><td>YES</td><td>NO</td><td>NO</td><td>NO</td><td>NO</td><td>NO</td><td>NO</td></tr>
      <tr><td class="row">HR Variability Analysis</td><td>YES</td><td>NO</td><td>NO</td><td>NO</td><td>NO</td><td>NO</td><td>NO</td></tr>
      <tr><td class="row">Sleep Apnea Detection</td><td>YES</td><td>NO</td><td>NO</td><td>NO</td><td>NO</td><td>NO</td><td>NO</td></tr>
      <tr><td class="row">SAECG Late Potentials</td><td>YES</td><td>NO</td><td>NO</td><td>NO</td><td>NO</td><td>NO</td><td>NO</td></tr>
      <tr><td class="row">A-Fib editing minute by minute by clinic</td><td>YES</td><td>NO</td><td>NO</td><td>NO</td><td>NO</td><td>NO</td><td>NO</td></tr>
    </table>
  </section>

  <section class="panel bg-blue">
    <h2 class="heading light" style="top:18px">T-Wave Alternans (TWA)</h2>
    <div class="screen twa" role="img" aria-label="Software screenshot of ECG strips with T-wave alternans measurements"></div>
    <ul class="points twa">
      <li>TWA occurs very often, and why hide it from cardiologists.</li>
      <li>It is included in the Holter processing of each patient.</li>
      <li>Each T-wave in each ECG Lead is analyzed for the amplitude of the T-wave.</li>
      <li>The Holter process takes less than 30-seconds to locate and display the ECGs showing TWA.</li>
    </ul>
  </section>

  <section class="panel bg-white">
    <h2 class="heading right" style="top:34px">The Very Best in Atrial Fib</h2>
    <div class="screen afib" role="img" aria-label="Software screenshot of atrial fibrillation ECG trends"></div>
    <ul class="points afib">
      <li>A-Fib detection is found in both the real-time ECG Trends and the Holter processing.</li>
      <li>The A-Fib verification and editing are excellent....the best available.</li>
      <li>A-Fib Burden is provided.</li>
      <li>A unique time display shows the length of each A-Fib event.</li>
    </ul>
  </section>

  <section class="panel bg-bands">
    <h2 class="label-box bottom">Competitive Comparisons continued…(Norquel, if informed by e-mail, will make any appropriate changes</h2>
    <div class="sheet"></div>
    <table class="compare bottom">
      <tr><th class="row"></th><th>Ostrel Telemetry</th><th>Dune Harbor Model A3</th><th>Velmora Unit 10</th><th>Pexano Line S</th><th>Taplor Patch X</th><th>Halvix Band R</th><th>Brovaline Strip M</th></tr>
      <tr><td class="row">Symptomatic events shown in real time</td><td>YES</td><td>NO</td><td>NO</td><td>NO</td><td>NO</td><td>NO</td><td>NO</td></tr>
      <tr><td class="row">24/7 live monitoring center with ECG view</td><td>YES</td><td>NO</td><td>NO</td><td>NO</td><td>NO</td><td>NO</td><td>NO</td></tr>
      <tr><td class="row">Full disclosure ECG for every minute of study</td><td>YES</td><td>NO</td><td>NO</td><td>NO</td><td>NO</td><td>NO</td><td>NO</td></tr>
      <tr><td class="row">Patient event notes sent from recorder</td><td>YES</td><td>NO</td><td>NO</td><td>NO</td><td>NO</td><td>NO</td><td>NO</td></tr>
      <tr><td class="row">Multi-lead ECG with ST analysis per lead</td><td>YES</td><td>NO</td><td>NO</td><td>NO</td><td>NO</td><td>NO</td><td>NO</td></tr>
      <tr><td class="row">Daily reports e-mailed to the physician</td><td>YES</td><td>NO</td><td>NO</td><td>NO</td><td>NO</td><td>NO</td><td>NO</td></tr>
      <tr><td class="row">ECG stored thirty days for clinic review</td><td>YES</td><td>NO</td><td>NO</td><td>NO</td><td>NO</td><td>NO</td><td>NO</td></tr>
      <tr><td class="row">End of study summary with A-Fib Burden</td><td>YES</td><td>NO</td><td>NO</td><td>NO</td><td>NO</td><td>NO</td><td>NO</td></tr>
      <tr><td class="row">Software and rhythm training for staff</td><td>YES</td><td>NO</td><td>NO</td><td>NO</td><td>NO</td><td>NO</td><td>NO</td></tr>
    </table>
  </section>

  <section class="panel bg-white">
    <h2 class="heading" style="top:18px">Elongated QTc</h2>
    <div class="screen qtc" role="img" aria-label="Software screenshot of ECG strips with QTc measurements"></div>
    <ul class="points qtc">
      <li>QTc analysis is provided for all ECG complexes during the monitoring time period.</li>
      <li>Finding the Elongated QTc is a simple and quick process.</li>
      <li>An electronic ruler is provided for verification of the data.</li>
      <li>The yellow arrow is the 50% of R-R.</li>
    </ul>
  </section>

  <section class="panel bg-bands">
    <div class="screen report" role="img" aria-label="Sample Holter end of study report page"></div>
  </section>

  <svg class="chevron left" viewBox="0 0 16 44" aria-hidden="true"><polyline points="14,2 3,22 14,42" fill="none" stroke="#ffffff" stroke-width="2.5"/></svg>
  <svg class="chevron right" viewBox="0 0 16 44" aria-hidden="true"><polyline points="2,2 13,22 2,42" fill="none" stroke="#ffffff" stroke-width="2.5"/></svg>
</main>
</body>
</html>
```